Fahrzeugbeschriftung: Heizung - Sanitär
Zielgruppe
Wir sind ein junger Meisterbetrieb der Heizungs- und Sanitärbranche und im Rhein-Main-Gebiet für unsere Kunden im Einsatz.
Wir benötigen eine Fahrzeugbeschriftung, die auffällig und modern, jedoch nicht zu verspielt und bunt ist.
Die Beschriftung soll für einen weißen Brava M3 Kasten sein. Es sollten alle Seiten des Fahrzeugs beschriftet werden.
Aufgabenstellung
Die Farbgebung sollte sich am dem Farben des Logos orientieren. Das Firmenlogo sollte im Vordergrund stehen. Auch die Worte Heizung, Sanitär, Solar sollten hervorstechen und gut erkennbar sein. Zusätzlich sollte der Begriff Meisterbetrieb verwendet werden.

```html
<!DOCTYPE html>
<html lang="de">
<head>
<meta charset="utf-8">
<title>HALDIG Haustechnik – Fahrzeugbeschriftung</title>
<link href="https://fonts.googleapis.com/css2?family=Montserrat:wght@700;800&display=swap" rel="stylesheet">
<style>
  :root {
    --navy: #08305a;
    --teal: #1d8a9c;
    --grey: #85888c;
    --white: #ffffff;
    --panel: #f4f5f6;
    --stage: #ffffff;
  }
  html, body {
    margin: 0;
    padding: 0;
    width: 1200px;
    height: 675px;
    overflow: hidden;
    background: var(--stage);
    font-family: "Montserrat", Arial, sans-serif;
  }
  .livery {
    position: relative;
    width: 1200px;
    height: 675px;
  }
  .livery-bands {
    position: absolute;
    inset: 0;
  }
  .slant {
    position: absolute;
    transform-origin: left bottom;
    white-space: nowrap;
    transform: rotate(-8deg);
  }
  .brand-name {
    left: 520px;
    top: 215px;
    font-weight: 800;
    font-size: 100px;
    line-height: 1;
    color: var(--navy);
    letter-spacing: 1px;
  }
  .brand-sub {
    left: 536px;
    top: 322px;
    font-weight: 700;
    font-size: 52px;
    line-height: 1;
    color: var(--teal);
    letter-spacing: 24px;
  }
  .services {
    left: 540px;
    top: 396px;
    font-weight: 700;
    font-size: 36px;
    line-height: 1;
    color: var(--grey);
    word-spacing: 10px;
  }
  .web {
    left: 532px;
    top: 480px;
    font-weight: 700;
    font-size: 21px;
    line-height: 1;
    color: var(--white);
    letter-spacing: 0.5px;
    transform: rotate(-8.6deg);
  }
  .logo-mark {
    position: absolute;
    left: 300px;
    top: 360px;
    display: flex;
    align-items: center;
    gap: 10px;
  }
  .logo-square {
    width: 22px;
    height: 22px;
    background: var(--navy);
  }
  .logo-name {
    font-weight: 800;
    font-size: 34px;
    color: var(--navy);
    line-height: 1;
  }
</style>
</head>
<body>
  <main class="livery">
    <svg class="livery-bands" width="1200" height="675" viewBox="0 0 1200 675" aria-hidden="true">
      <rect class="side-panel" x="40" y="150" width="1120" height="365" rx="18" fill="var(--panel)"/>
      <polygon class="band-top" points="40,168 58,150 850,150 40,240" fill="var(--teal)"/>
      <polygon class="band-bottom" points="300,490 1160,360 1160,497 1142,515 300,515" fill="var(--navy)"/>
    </svg>

    <div class="logo-mark">
      <span class="logo-square"></span>
      <span class="logo-name">HALDIG</span>
    </div>

    <div class="slant brand-name">HALDIG</div>
    <div class="slant brand-sub">Haustechnik</div>
    <div class="slant services">•Heizung •Sanitär •Solar</div>
    <div class="slant web">www.haldig-haustechnik.de</div>
  </main>
</body>
</html>
```